Exciting New Reseller Brand requires Website to WOW New clients to register.

We are a NEW online business called Trade Your Goods.

The Website is a simple concept, it looks to put Merchants (businesses that want their products resold) in touch with Resellers (people or businesses that want to resell that product).

The website acts as an online market place which looks to get Merchants to sign-up and pay to list their company and product as well as getting Resellers to sign-up to view potential Merchants they can get in touch with in the right industry or area to resell their products for (see attached slide-pack to explain packages)

Any type of Industry or Business can register themselves to get listed on Trade Your Goods to see either get their product/service resold or to look for products / services to reseller.

Trade Your Goods does not take any other monetary part in the business relationships other than to obtain money for the monthly website subscription.

We want a very simple website, so this project is for several pages:

Page 1) A really vibrant, exciting, image based homepage to get people to sign-up / register (see sites that we like in the project brief). Needs to be very clear that there are 2 customers and to sign up to join, build and earn!

Page 2) A page that describes the benefits and packages for Resellers.

Page 3) A page that describes the benefits and packages for Merchants.

Page 4) The Payment process pages, taking the customer through sign-up

Page 5) The Business Listings page, so when people search for a Merchant how this will be displayed.

We would really like an image based site and preferably parallax. We want it bright vibrant and to look like a social media site.

All necessary files / logos enclosed.

We would love to continue to work with the winning designer moving forward.

Many thanks and Good Luck.

Regards

Martin & Owen

Target Market(s)

Merchants, Suppliers, Vendors, Manufacturers, Distributors, Wholesalers, Affiliate programs, Franchisees, Reselers

Industry/Entity Type

Business

Number of Pages Required

5+ page

Requirements
Must have
• We love the following websites:
• 1) Like the top section, i.e. parallax image based: www.brightfoxstudio.co.uk
• 2) Like the way the screen is split in 2, could be used to describe the 2 different customers we are after Merchants / Resellers: www.cloudtrunk.example/guide
• 3) Like the bright colours / full screen video split into 2 below top banner and the generally how simple the site is: www.harbourlinden.com.au
• 4) Love all of this site, simple, bold, Love the colours, the clear message and the infographics: http://www.velomiro.example/swiftride/quicker

```html
<!DOCTYPE html>
<html lang="en">
<head>
<meta charset="utf-8">
<title>Trade Your Goods</title>
<link href="https://fonts.googleapis.com/css2?family=Lato:wght@400;700;900&family=Oswald:wght@500&display=swap" rel="stylesheet">
<style>
:root{
  --blue:#1588d0;
  --blue-deep:#0a6fb3;
  --green:#8dc63f;
  --navy:#0d3a66;
  --ink:#222;
  --grey:#555;
  --black:#000;
  --white:#fff;
}
*{margin:0;padding:0;box-sizing:border-box}
html,body{width:1200px;height:3854px;overflow:hidden}
body{position:relative;font-family:'Lato',sans-serif;color:var(--ink);background:var(--white)}
.abs{position:absolute}
svg.defs{position:absolute;width:0;height:0}

/* hero */
.hero{position:absolute;left:0;top:0;width:1200px;height:643px;overflow:hidden}
.hero-photo{position:absolute;inset:0;background:
  radial-gradient(ellipse 520px 300px at 140px 620px,rgba(10,16,24,.75) 0,rgba(10,16,24,.35) 55%,transparent 100%),
  radial-gradient(circle at 770px 250px,#ffffff 0,#e8f4ff 60px,#8cc7f0 200px,transparent 420px),
  linear-gradient(180deg,#1f6fc0 0%,#3f92dc 45%,#8cc3ec 80%,#c6e2f6 100%)}
.brand{position:absolute;left:134px;top:22px;display:flex;align-items:center;gap:12px}
.brand-dot{width:50px;height:50px;border-radius:50%;background:var(--green)}
.brand-name{font-weight:900;font-size:34px;color:var(--navy);letter-spacing:-.5px}
.account{position:absolute;top:0;left:866px;display:flex;gap:6px}
.account a{display:block;height:26px;line-height:26px;padding:0 22px;font-size:12px;font-weight:700;color:var(--white);text-decoration:none;border-radius:0 0 6px 6px}
.account .signup{background:var(--blue)}
.account .login{background:var(--green)}
.mainnav{position:absolute;top:48px;left:530px;display:flex;font-size:14px}
.mainnav a{color:var(--navy);text-decoration:none;padding:0 10px;border-left:1px solid rgba(13,58,102,.4);line-height:16px}
.mainnav a:first-child{border-left:0;font-weight:700;padding-left:5px;border-bottom:2px solid var(--navy)}
.hero-title{position:absolute;left:578px;top:366px;font-family:'Oswald',sans-serif;font-weight:500;color:#1b2530;line-height:1.05}
.hero-title .l1{font-size:42px;display:block}
.hero-title .l2{font-size:54px;display:block;margin-top:6px}
.steps{position:absolute;left:578px;top:524px}
.dots{position:absolute;left:586px;top:612px;display:flex;gap:6px}
.dots span{width:16px;height:16px;border-radius:50%;border:2px solid var(--white)}
.dots span:first-child{background:var(--blue);border-color:var(--blue)}

/* about */
.about{position:absolute;left:0;top:643px;width:1200px;height:347px;background:linear-gradient(180deg,#1b9be0 0%,#0f7fcb 100%);color:var(--white);text-align:center}
.about h2{margin-top:40px;font-size:26px;font-weight:900;letter-spacing:.5px}
.about p{width:1002px;margin:66px auto 0;font-size:13.5px;line-height:21px}

/* sections */
.section-title{position:absolute;left:0;width:1200px;text-align:center;font-size:28px;font-weight:900;letter-spacing:.5px}
.rule{position:absolute;left:130px;width:936px;height:1px}
.rule::before,.rule::after{content:"";position:absolute;top:0;height:1px;width:430px;background:currentColor}
.rule::before{left:0}.rule::after{right:0}

.resellers{position:absolute;left:0;top:990px;width:1200px;height:843px;background:var(--black)}
.merchants{position:absolute;left:0;top:1833px;width:1200px;height:867px;background:var(--white)}

.benefits{position:absolute;width:300px}
.benefits h3{font-size:18px;font-weight:900;letter-spacing:1px;padding-bottom:12px;border-bottom:1px solid}
.benefits ul{list-style:none;margin-top:18px}
.benefits li{font-size:16.5px;line-height:35px}
.benefits li::before{content:"";display:inline-block;border-left:7px solid currentColor;border-top:5px solid transparent;border-bottom:5px solid transparent;margin-right:12px}

.price{position:absolute;left:131px;width:938px;height:363px;background:var(--green)}
.price h4{position:absolute;top:18px;width:100%;text-align:center;font-size:18px;font-weight:900;color:var(--ink);letter-spacing:.5px}
.plan-list{position:absolute;left:23px;top:70px;width:285px}
.plan-list h5{font-size:18px;font-weight:900;color:var(--navy);padding-bottom:12px;border-bottom:1px solid var(--navy)}
.plan-list ul{list-style:none;margin-top:10px}
.plan-list li{font-size:15.5px;font-weight:700;color:var(--navy);line-height:35px}
.plan-list li::before{content:"";display:inline-block;border-left:6px solid var(--navy);border-top:4px solid transparent;border-bottom:4px solid transparent;margin-right:10px}
.tiers{position:absolute;left:332px;top:74px;width:583px;height:255px;display:grid;grid-template-columns:repeat(3,1fr);border:3px solid var(--black);background:var(--white)}
.tier{display:flex;flex-direction:column;border-left:1px solid #bbb}
.tier:first-child{border-left:0}
.tier .th,.tier .tf{height:36px;line-height:36px;text-align:center;background:var(--black);color:var(--white);font-weight:900;font-size:18px}
.tier.mid .th,.tier.mid .tf{background:var(--blue)}
.tier.mid{border-left:2px solid var(--blue);border-right:2px solid var(--blue)}
.tier .ticks{flex:1;display:flex;flex-direction:column;align-items:center;padding-top:12px}
.tier .ticks svg{width:20px;height:20px;margin-bottom:13px}
.price .note{position:absolute;top:336px;width:100%;text-align:center;font-size:14px;font-weight:700;color:var(--ink)}

.photo{position:absolute}

/* showcase */
.showcase{position:absolute;left:0;top:2700px;width:1200px;height:513px;background:linear-gradient(90deg,#5c341c 0%,#8a5533 35%,#a26a42 55%,#7b4a2a 80%,#5a321b 100%)}
.screen{position:absolute;left:128px;top:45px;width:502px;height:330px;border-radius:14px;background:linear-gradient(135deg,#1c2470 0%,#4b2fa4 45%,#2a6fd6 100%);border:14px solid #111}
.stand{position:absolute;left:300px;top:375px;width:160px;height:70px;background:linear-gradient(180deg,#c9c9c9,#9c9c9c)}
.stand-base{position:absolute;left:255px;top:442px;width:250px;height:12px;border-radius:4px;background:#bdbdbd}
.features{position:absolute;left:694px;top:2862px;list-style:none;color:var(--white)}
.features li{font-size:16px;font-weight:700;line-height:41px}
.features li::before{content:"";display:inline-block;border-left:7px solid var(--white);border-top:5px solid transparent;border-bottom:5px solid transparent;margin-right:10px}

/* how it works */
.flow-head{position:absolute;height:56px;line-height:56px;text-align:center;color:var(--white);font-size:24px;font-weight:700}
.flow-box{position:absolute;height:61px;line-height:57px;text-align:center;font-size:24px;font-weight:700;background:var(--white)}
.flow-label{position:absolute;font-size:24px;font-weight:700;text-align:center}
.promote{position:absolute;left:342px;top:3703px;width:496px;height:62px;line-height:58px;text-align:center;border:2px solid var(--blue);font-size:27px;font-weight:700;color:var(--blue);letter-spacing:1px}
.promote span{color:var(--green)}

/* footer */
.footer{position:absolute;left:0;top:3796px;width:1200px;height:58px;background:var(--green)}
.footer nav{position:absolute;left:134px;top:10px;font-size:12px;color:var(--navy)}
.footer nav a{color:var(--navy);text-decoration:none;padding:0 8px;border-left:1px solid var(--navy)}
.footer nav a:first-child{border-left:0;padding-left:0}
.footer small{position:absolute;left:134px;top:32px;font-size:12px;color:var(--navy)}
.social{position:absolute;left:935px;top:14px;display:flex;gap:6px}
.social span{width:30px;height:30px;border-radius:50%;background:#5a5a5a}
</style>
</head>
<body>
<svg class="defs" aria-hidden="true"><defs>
  <symbol id="tick" viewBox="0 0 20 20"><rect x="1" y="5" width="13" height="13" fill="none" stroke="#777" stroke-width="1.3"/><path d="M4 11l4 4 10-12" fill="none" stroke="#555" stroke-width="2.2"/></symbol>
</defs></svg>

<header class="hero">
  <div class="hero-photo" role="img" aria-label="Photo of a person standing on a clifftop against a bright sunlit sky"></div>
  <div class="brand"><span class="brand-dot"></span><span class="brand-name">Trade Your Goods</span></div>
  <div class="account"><a class="signup" href="#">SIGN UP</a><a class="login" href="#">LOGIN</a></div>
  <nav class="mainnav"><a href="#">Home</a><a href="#">For Resellers</a><a href="#">For Merchants</a><a href="#">Payment Process</a><a href="#">Business Listings</a></nav>
  <h1 class="hero-title"><span class="l1">Building your own</span><span class="l2">Virtual Sales Team</span></h1>
  <svg class="steps" width="400" height="48" viewBox="0 0 400 48">
    <polygon points="0,0 124,0 140,24 124,48 0,48" fill="#2b2f33"/>
    <polygon points="132,0 262,0 278,24 262,48 132,48 148,24" fill="#8dc63f"/>
    <polygon points="270,0 384,0 400,24 384,48 270,48 286,24" fill="#2b2f33"/>
    <g font-family="Oswald,sans-serif" font-size="28" fill="#fff" text-anchor="middle">
      <text x="64" y="34">join</text><text x="207" y="34">build</text><text x="338" y="34">earn</text>
    </g>
  </svg>
  <div class="dots"><span></span><span></span><span></span><span></span></div>
</header>

<section class="about">
  <h2>ABOUT TRADE YOUR GOODS</h2>
  <p>Lorem ipsum dolor sit amet, consectetuer adipiscing elit, sed diam nonummy nibh euismod tincidunt ut laoreet dolore magna aliquam erat volutpat. Ut wisi enim ad minim veniam, quis nostrud exerci tation ullamcorper suscipit lobortis nisl ut aliquip ex ea commodo consequat. Duis autem vel eum iriure dolor in hendrerit in vulputate velit esse molestie consequat, vel illum dolore eu feugiat nulla facilisis at vero eros et accumsan et iusto odio dignissim qui blandit praesent luptatum zzril delenit augue duis dolore te feugait nulla facilisi. Lorem ipsum dolor sit amet, consectetuer adipiscing elit, sed diam nonummy nibh euismod tincidunt ut laoreet dolore magna aliquam erat volutpat. Ut wisi enim ad minim veniam, quis nostrud exerci tation. Lorem ipsum dolor sit amet, consectetuer adipiscing elit, sed diam nonummy nibh euismod tincidunt ut laoreet dolore magna aliquam erat volutpat. Ut wisi enim ad minim veniam, quis nostrud exerci tation ullamcorper suscipit lobortis nisl ut aliquip ex ea commodo consequat. Duis autem v</p>
</section>

<section class="resellers">
  <h2 class="section-title" style="top:36px;color:var(--white)">FOR <span style="color:var(--green)">RESELLERS</span></h2>
  <div class="rule" style="top:102px;color:#333"></div>
  <div class="photo" role="img" aria-label="Young plant growing from a pile of coins" style="left:334px;top:140px;width:309px;height:232px;background:radial-gradient(ellipse at 50% 40%,#4f8a22 0,#2d5a14 30%,transparent 55%),radial-gradient(ellipse at 50% 85%,#b08a3c 0,#6d5020 40%,#000 70%)"></div>
  <div class="benefits" style="left:700px;top:180px;color:var(--white)">
    <h3 style="color:var(--green);border-color:#555">BENEFITS</h3>
    <ul><li>Additional Stream of Income</li><li>Infrastructure in Place</li><li>No Additional Cost</li><li>Expand Product Suite</li><li>Reach New Target Markets</li></ul>
  </div>
  <div class="price" style="top:447px">
    <h4>PRODUCT PRICE STRUCTURE</h4>
    <div class="plan-list"><h5>RESELLERS</h5>
      <ul><li>Search Merchant Database</li><li>Reseller Listing</li><li>Monthly Newsletters</li><li>Seminars &amp; Network Events</li><li>Dedicated Merchant Scout</li></ul>
    </div>
    <div class="tiers">
      <div class="tier"><div class="th">Tier 1</div><div class="ticks"><svg><use href="#tick"/></svg></div><div class="tf">FREE</div></div>
      <div class="tier mid"><div class="th">Tier 2</div><div class="ticks"><svg><use href="#tick"/></svg><svg><use href="#tick"/></svg><svg><use href="#tick"/></svg></div><div class="tf">£25 p/month</div></div>
      <div class="tier"><div class="th">Tier 2</div><div class="ticks"><svg><use href="#tick"/></svg><svg><use href="#tick"/></svg><svg><use href="#tick"/></svg><svg><use href="#tick"/></svg><svg><use href="#tick"/></svg></div><div class="tf">£100 p/month</div></div>
    </div>
    <p class="note">All are minimum of 12 months, discounts for 24 months.</p>
  </div>
</section>

<section class="merchants">
  <h2 class="section-title" style="top:30px;color:var(--ink)">FOR <span style="color:var(--blue)">MERCHANTS</span></h2>
  <div class="rule" style="top:99px;color:#e4e4e4"></div>
  <div class="photo" role="img" aria-label="Business handshake in front of an office building" style="left:226px;top:159px;width:494px;height:260px;background:linear-gradient(120deg,#1a1a1a 0%,#3a4048 30%,#b9c6d2 55%,#e8edf1 70%,#2a2d31 100%)"></div>
  <div class="benefits" style="left:756px;top:185px;color:var(--grey)">
    <h3 style="color:var(--blue);border-color:#ccc">BENEFITS</h3>
    <ul><li>Additional Stream of Income</li><li>Infrastructure in Place</li><li>No Additional Cost</li><li>Expand Product Suite</li><li>Reach New Target Markets</li></ul>
  </div>
  <div class="price" style="top:452px">
    <h4>PRODUCT PRICE STRUCTURE</h4>
    <div class="plan-list"><h5>MERCHANTS</h5>
      <ul><li>Directory Listing</li><li>Monthly Newsletters</li><li>Seminars &amp; Network Events</li><li>Onsite Advertising</li><li>Dedicated Reseller Scout</li></ul>
    </div>
    <div class="tiers">
      <div class="tier"><div class="th">Tier 1</div><div class="ticks"><svg><use href="#tick"/></svg></div><div class="tf">£50 p/month</div></div>
      <div class="tier mid"><div class="th">Tier 2</div><div class="ticks"><svg><use href="#tick"/></svg><svg><use href="#tick"/></svg><svg><use href="#tick"/></svg></div><div class="tf">£150 p/month</div></div>
      <div class="tier"><div class="th">Tier 2</div><div class="ticks"><svg><use href="#tick"/></svg><svg><use href="#tick"/></svg><svg><use href="#tick"/></svg><svg><use href="#tick"/></svg><svg><use href="#tick"/></svg></div><div class="tf">£300 p/month</div></div>
    </div>
    <p class="note">All are minimum of 12 months, discounts for 24 months.</p>
  </div>
</section>

<section class="showcase" role="img" aria-label="Wooden plank wall background">
  <div class="screen" role="img" aria-label="Desktop monitor showing the website homepage"></div>
  <div class="stand"></div>
  <div class="stand-base"></div>
</section>
<ul class="features">
  <li>Portal for Resellers and Merchants.</li>
  <li>Merchants can promote their products.</li>
  <li>Merchants can build a virtual sales team.</li>
  <li>Resellers can expand product portfolio.</li>
  <li>Resellers can generate revenue.</li>
  <li>Industry news and opportunities.</li>
</ul>

<section class="how">
  <h2 class="section-title" style="top:3252px;color:var(--ink)">HOW <span style="color:var(--blue)">IT WORKS</span></h2>
  <div class="rule" style="top:3316px;color:#e4e4e4"></div>
  <div class="flow-head" style="left:229px;top:3367px;width:324px;background:var(--blue-deep)">Merchants</div>
  <div class="flow-head" style="left:635px;top:3367px;width:324px;background:var(--green)">Resellers</div>
  <div class="flow-box" style="left:229px;top:3480px;width:330px;border:2px solid var(--blue);color:var(--blue)">Payment</div>
  <div class="flow-box" style="left:633px;top:3480px;width:326px;border:2px solid var(--blue);color:var(--blue)">Register</div>
  <svg class="abs" style="left:350px;top:3560px" width="60" height="90" viewBox="0 0 60 90"><polygon points="15,0 45,0 45,50 60,50 30,88 0,50 15,50" fill="#0a6fb3"/></svg>
  <svg class="abs" style="left:762px;top:3560px" width="60" height="90" viewBox="0 0 60 90"><polygon points="15,0 45,0 45,50 60,50 30,88 0,50 15,50" fill="#8dc63f"/></svg>
  <div class="flow-label" style="left:300px;top:3655px;width:160px;color:var(--blue)">Listing</div>
  <div class="flow-label" style="left:712px;top:3655px;width:160px;color:var(--blue)">Search</div>
  <div class="promote">Promote<span>and</span>earn</div>
</section>

<footer class="footer">
  <nav><a href="#">Home</a><a href="#">For Resellers</a><a href="#">For Merchants</a><a href="#">Payment Process</a><a href="#">Business Listings</a></nav>
  <small>©2015 Tradeyourgoods.example | All Rights Reserved.</small>
  <div class="social"><span></span><span></span><span></span><span></span></div>
</footer>
</body>
</html>
```